Spice Mix Label Bottle Branding - Health and Weight Loss Mixes

The company is called ZestRow Spice Mix's. We've created 5 spice mixes using ingredients that promote health and weight loss. We already have a logo but now we need labels for our bottles. We would like to see designs that have the feel of health supplements (see attached examples)

We would like a different colour featured with each of our flavours.

Our flavours are:
-Golden Chai (Yellow)
-Mild Curry (Orange)
-Coffee Rub (brown)
-Garlic Oregano (Green)
-Taco (Blue)

Thank you!

Target Market(s)

Ages 22-35. Men and Female. Trendy, Hipster.

Industry/Entity Type

Food Production

Font styles to use
Sans Serif

Colors
f37122
0655a3
0692cd
9bcb3c
fbee3f

Requirements
Must have
• A different featured colour for each flavour.
• The ZestRow Spices Logo (attached)
• The slogan: "Weight Loss Ingredients"
• -Golden Chai (Yellow)
• -Mild Curry (Orange)
• -Coffee Rub (brown)
• -Garlic Oregano (Green)
• -Taco (Blue)
• Text Files attached.
Nice to have
• A black label with a featured colour for each of the spice mice flavours.
• 'No Salt added'

```html
<!DOCTYPE html>
<html lang="en">
<head>
<meta charset="utf-8">
<title>ZestRow Spices – Label Set</title>
<link rel="stylesheet" href="https://fonts.googleapis.com/css2?family=Bebas+Neue&family=Oswald:wght@700&family=Montserrat:wght@700&display=swap">
<style>
  :root {
    --bg: #ececec;
    --label: #ffffff;
    --ink: #1a1a1a;
    --coffee: #b0824a;
    --coffee-tint: #e6d3b8;
    --taco: #3a76b4;
    --taco-tint: #b9cfe6;
    --curry: #f37122;
    --curry-tint: #f9c3a0;
  }
  * { box-sizing: border-box; margin: 0; padding: 0; }
  html, body { width: 1200px; height: 802px; overflow: hidden; }
  body {
    background: var(--bg);
    display: flex;
    align-items: center;
    justify-content: center;
    gap: 60px;
  }
  .label {
    position: relative;
    width: 320px;
    height: 360px;
    background: var(--label);
    overflow: hidden;
    box-shadow: 0 2px 10px rgba(0,0,0,0.06);
  }
  .label__pattern {
    position: absolute;
    inset: 0;
    width: 100%;
    height: 100%;
  }
  .label__panel {
    position: absolute;
    left: 50%;
    top: 50%;
    width: 224px;
    height: 228px;
    transform: translate(-50%, -50%);
    background: var(--label);
    border: 1px solid var(--accent);
    display: flex;
    flex-direction: column;
    align-items: center;
    justify-content: center;
    text-align: center;
  }
  .brand { display: flex; flex-direction: column; align-items: center; }
  .brand__mark {
    width: 10px; height: 10px;
    background: var(--accent);
    border-radius: 50%;
    margin-bottom: 8px;
  }
  .brand__name {
    font-family: "Oswald", sans-serif;
    font-weight: 700;
    font-size: 34px;
    line-height: 1;
    letter-spacing: 0.5px;
    color: var(--ink);
    text-transform: uppercase;
  }
  .brand__tagline {
    margin-top: 6px;
    padding-top: 4px;
    border-top: 1.5px solid var(--ink);
    font-family: "Montserrat", sans-serif;
    font-weight: 700;
    font-size: 7px;
    letter-spacing: 0.2px;
    color: var(--ink);
    text-transform: uppercase;
  }
  .flavour {
    margin-top: 22px;
    font-family: "Bebas Neue", sans-serif;
    font-size: 40px;
    line-height: 1;
    color: var(--accent);
  }
  .label--coffee { --accent: var(--coffee); --tint: var(--coffee-tint); }
  .label--taco   { --accent: var(--taco);   --tint: var(--taco-tint); }
  .label--curry  { --accent: var(--curry);  --tint: var(--curry-tint); }
</style>
</head>
<body>

  <section class="label label--coffee">
    <svg class="label__pattern" viewBox="0 0 320 360" role="img" aria-label="Wave-scale decorative pattern in coffee brown">
      <circle cx="150" cy="215" r="150" fill="var(--coffee-tint)"/>
    </svg>
    <div class="label__panel">
      <div class="brand">
        <span class="brand__mark"></span>
        <span class="brand__name">ZestRow Spices</span>
        <span class="brand__tagline">Weight Loss Seasonings</span>
      </div>
      <h2 class="flavour">Coffee Rub</h2>
    </div>
  </section>

  <section class="label label--taco">
    <svg class="label__pattern" viewBox="0 0 320 360" role="img" aria-label="Swirling droplet decorative pattern in blue">
      <circle cx="175" cy="200" r="140" fill="var(--taco-tint)"/>
    </svg>
    <div class="label__panel">
      <div class="brand">
        <span class="brand__mark"></span>
        <span class="brand__name">ZestRow Spices</span>
        <span class="brand__tagline">Weight Loss Seasonings</span>
      </div>
      <h2 class="flavour">Taco</h2>
    </div>
  </section>

  <section class="label label--curry">
    <svg class="label__pattern" viewBox="0 0 320 360" role="img" aria-label="Flowing paisley decorative pattern in orange">
      <circle cx="230" cy="190" r="150" fill="var(--curry-tint)"/>
    </svg>
    <div class="label__panel">
      <div class="brand">
        <span class="brand__mark"></span>
        <span class="brand__name">ZestRow Spices</span>
        <span class="brand__tagline">Weight Loss Seasonings</span>
      </div>
      <h2 class="flavour">Mild Curry</h2>
    </div>
  </section>

</body>
</html>
```